Dental Brochure for New Dental Advertising Company

Please create a beautiful brochure design based on the rough outlines provided. I'd like for the brochure design to be modern with strong graphic usage and clean fonts. Large pictures of pretty people smiling.

Feel free to arrange items as you see fit. I have attached a historical brochure for layout reference mainly- I do need mailing panel laid out similarly as KRDM will need the indicia in the top right corner with address box below and return address info next to indicia.

Id like a format that I can use to edit in Adobe programs in the future.

The size of layout is 9 "x 15" that folds into a 9" x 5" brochure.

Target Market(s)

Dental Consumer

Industry/Entity Type

Dental

Requirements
Nice to have
• Dentists love big pictures of people smiling. Simple layout with easy to read content.

```html
<!DOCTYPE html>
<html lang="en">
<head>
<meta charset="utf-8">
<title>Maple Ridge Family Dental – Trifold Brochure</title>
<link href="https://fonts.googleapis.com/css2?family=Tinos:ital,wght@0,400;0,700;1,400;1,700&family=Arimo:wght@400;700&display=swap" rel="stylesheet">
<style>
:root{
  --navy:#3b2b8c;
  --green:#3aa54a;
  --ink:#2b2b33;
  --sky:#d6ebf8;
  --sky-deep:#a9d2ee;
  --paper:#f6fafd;
  --canvas:#eeeff1;
  --skin:#e2b497;
  --skin-light:#f2d9c6;
  --serif:'Tinos', 'Times New Roman', serif;
  --sans:'Arimo', Arial, sans-serif;
}
*{box-sizing:border-box;margin:0;padding:0}
html,body{width:755px;height:1200px;overflow:hidden;background:var(--canvas)}
.sheet{position:absolute;left:20px;width:715px;height:429px;display:flex;
  box-shadow:0 4px 14px rgba(0,0,0,.15);background:var(--paper)}
.sheet--outside{top:150px}
.sheet--inside{top:620px}
.panel{position:relative;width:33.333%;height:100%;overflow:hidden;
  background:linear-gradient(160deg,#ffffff 0%,#eef6fc 45%,var(--sky) 100%);
  text-align:center;font-family:var(--sans);color:var(--ink)}
.panel::before{content:"";position:absolute;left:-20%;right:-20%;top:-40px;height:90px;
  background:linear-gradient(90deg,rgba(169,210,238,.55),rgba(255,255,255,0));border-radius:50%;transform:rotate(-6deg)}
.panel > *{position:relative}
.panel--cover{background:linear-gradient(170deg,#f4f7fa 0%,#e4ebf1 50%,#d5e7f4 100%)}
.panel--smile{background:linear-gradient(180deg,#fbfdff 0%,#eef6fc 55%,#c6e0f2 100%)}
.head{font-family:var(--serif);font-weight:700;color:var(--navy);font-size:15px;line-height:1.15}
.sub{font-family:var(--serif);font-weight:700;color:var(--green);font-size:8px;line-height:1.2}
.body{font-size:6px;line-height:1.35}
.tiny{font-size:4.6px;line-height:1.35}
.brand{font-family:var(--serif);font-weight:700;color:var(--navy);font-size:13px;display:inline-flex;align-items:center;gap:5px}
.brand-dot{width:10px;height:10px;border-radius:50%;background:var(--green)}
.photo{position:absolute;display:block}
.photo--family{left:0;right:0;bottom:0;height:150px;
  background:
    radial-gradient(ellipse 40% 55% at 30% 45%,var(--skin) 0%,rgba(226,180,151,0) 70%),
    radial-gradient(ellipse 35% 50% at 75% 55%,var(--skin-light) 0%,rgba(242,217,198,0) 70%),
    linear-gradient(180deg,rgba(238,246,252,0) 0%,#cfe4f3 60%,#a9d2ee 100%)}
.photo--patient{left:84px;top:348px;width:66px;height:66px;border-radius:50%;border:2px solid var(--green);
  background:radial-gradient(circle at 65% 45%,var(--skin) 0%,#eadbd0 35%,#cfe6f4 70%,#b6d7ec 100%)}
.photo--mother{left:24px;right:0;top:56px;height:228px;
  background:
    radial-gradient(ellipse 38% 34% at 35% 38%,var(--skin) 0%,rgba(226,180,151,0) 75%),
    radial-gradient(ellipse 30% 30% at 72% 30%,var(--skin-light) 0%,rgba(242,217,198,0) 75%),
    linear-gradient(180deg,#e9eef2 0%,#dbe6ee 60%,#cfe1ef 100%)}
.cover-frame{position:absolute;left:10px;right:-14px;top:50px;height:240px;border:6px solid var(--green);border-radius:34px}
.photo--smile{left:0;right:0;top:0;height:175px;
  background:
    radial-gradient(ellipse 70% 30% at 45% 45%,#ffffff 0%,rgba(255,255,255,0) 60%),
    radial-gradient(ellipse 90% 70% at 40% 40%,var(--skin) 0%,var(--skin-light) 55%,rgba(242,217,198,0) 85%),
    linear-gradient(180deg,#f6e7dc,rgba(251,253,255,0))}
.pill{display:inline-block;background:var(--navy);color:#fff;font-family:var(--serif);font-size:6.5px;padding:4px 14px;border-radius:6px 6px 0 0}
.cta{display:inline-block;background:var(--green);color:#fff;font-family:var(--serif);font-weight:700;font-size:6.5px;padding:4px 12px;border-radius:4px}
.list{text-align:left;list-style:none;font-size:6px;line-height:1.3;padding:0 16px}
.list li{position:relative;padding-left:9px;margin-bottom:3px}
.list li::before{content:"";position:absolute;left:0;top:2px;width:4px;height:4px;background:var(--green)}
.rule{width:32px;height:2px;background:var(--green);margin:6px auto 0}
.vert{position:absolute;writing-mode:vertical-rl;transform:rotate(180deg);white-space:nowrap;text-align:left}
.indicia{position:absolute;left:136px;top:16px;width:16px;height:30px;border:.5px solid #999;background:#fff;
  font-size:3.4px;line-height:1.25;color:#555;writing-mode:vertical-rl;transform:rotate(180deg);padding:1px;text-align:center}
.tagline{font-family:var(--serif);font-style:italic;font-weight:700;color:var(--navy);font-size:12px;line-height:1.2}
.social{display:flex;justify-content:center;gap:6px;font-size:6px;color:var(--navy);font-weight:700}
</style>
</head>
<body>

<section class="sheet sheet--outside">
  <div class="panel panel--cleanings">
    <div style="padding:22px 12px 0">
      <h2 class="head">Stay Healthy With<br>Regular Cleanings!</h2>
      <p class="body" style="margin-top:8px">Cleanings Help Protect You &amp; Your Family From:<br>Heart Disease • Strokes • The Worsening of Asthma<br>The Worsening of Diabetes • Helps Ensure Healthy<br>Pregnancy Reduces Chances of Alzheimer's • Reduces<br>Chances of Dementia</p>
      <p class="body" style="margin-top:6px">Sources: National Oral Health Board, Westbrook University,<br>Dental School, Journal of Preventive Care,<br>Crestview Medicine, Coastal Dental Review &amp; Many More</p>
      <p class="body" style="margin-top:6px">copyright © 2022 brightline media, inc. oak county, all<br>rights reserved</p>
      <h3 class="head" style="margin-top:12px;font-size:14px">Emergency Dental<br>Care Available Today!</h3>
      <div class="rule"></div>
    </div>
    <div class="photo photo--family" role="img" aria-label="Photo of a smiling family of four, father carrying children"></div>
  </div>

  <div class="panel panel--mailing">
    <div class="vert" style="left:22px;top:60px;font-family:var(--serif);font-weight:700;color:var(--navy);font-size:6.5px">Maple Ridge Family Dental</div>
    <div class="vert body" style="left:36px;top:36px;font-size:6px;line-height:1.3">212 Linden Street, Suite 4,<br>Brookfield, NJ 07100<br>555-214-3860<br>MapleRidgeFamilyDental.com</div>
    <div class="vert body" style="left:100px;top:60px;font-size:5.5px">MAILING ADDRESS HERE</div>
    <div class="indicia">PRSRT STD<br>KRDM POSTAGE<br>PAID</div>
    <div class="vert tiny" style="left:196px;top:16px;font-size:3.4px;color:#555;line-height:1.3">This mailer is intended for local residents only. Offers may<br>vary by insurance plan. Not valid with other offers.<br>Please call for details and scheduling.</div>
    <div style="position:absolute;top:218px;left:0;right:0">
      <h3 class="tagline" style="font-size:11px">We Love Your Insurance!</h3>
      <p class="body" style="margin-top:3px">Most insured patients pay nothing out-of-pocket<br>for the services below:</p>
      <p style="font-family:var(--serif);font-size:7px;line-height:1.3;margin-top:5px">Brighter, Whiter Cleaning for Adults<br>Cleaning &amp; Exam for Children<br>Exam for Adults<br><b>FREE</b> Second Opinion Evaluation</p>
      <div class="social" style="margin-top:5px"><span>Linkora</span><span>|</span><span>Seekit</span></div>
    </div>
    <div class="photo photo--patient" role="img" aria-label="Circular photo of a dentist treating a smiling patient"></div>
  </div>

  <div class="panel panel--cover">
    <div style="padding:14px 0 0"><span class="brand"><span class="brand-dot"></span>Maple Ridge Family Dental</span></div>
    <div class="cover-frame"></div>
    <div class="photo photo--mother" role="img" aria-label="Photo of a smiling mother with her young daughter on her back"></div>
    <div style="position:absolute;top:298px;left:0;right:0">
      <p class="tagline">A 20-Year Brookfield<br>Tradition of Trusted &amp; Caring<br>Dental Excellence!</p>
      <p style="font-family:var(--serif);font-size:6.5px;margin-top:8px">Welcome Weekdays as Late as 6pm &amp; Saturdays!</p>
    </div>
    <div style="position:absolute;bottom:0;left:0;right:0"><span class="pill">www.mapleridgesmiles.com</span></div>
  </div>
</section>

<section class="sheet sheet--inside">
  <div class="panel panel--smile">
    <div class="photo photo--smile" role="img" aria-label="Close-up photo of a woman's bright white smile"></div>
    <div style="position:absolute;top:178px;left:0;right:0;padding:0 10px">
      <h2 class="head" style="font-size:13px">Stay Healthy With<br>Regular Cleanings!</h2>
      <p class="sub">Cleanings Help Protect You &amp;<br>Your Family From:</p>
      <p class="body" style="margin-top:5px">Heart Disease • Strokes • The Worsening of Asthma<br>The Worsening of Diabetes • Helps Ensure Healthy<br>Pregnancy Reduces Chances of Alzheimer's • Reduces<br>Chances of Dementia</p>
      <p class="body" style="margin-top:6px">Sources: National Oral Health Board, Westbrook University,<br>Dental School, Journal of Preventive Care,<br>Crestview Medicine, Coastal Dental Review &amp; Many More</p>
      <p class="tiny" style="margin-top:6px">copyright © 2022 brightline media, inc. oak county, all rights reserved</p>
      <h3 class="head" style="margin-top:10px;font-size:16px">We Love Kids &amp;<br>Families</h3>
      <p style="font-family:var(--serif);font-weight:700;font-size:10px;line-height:1.3;margin-top:2px">Welcome Weekdays<br>as Late as 6pm &amp; Saturdays!</p>
    </div>
  </div>

  <div class="panel panel--contact">
    <div style="padding:16px 12px 0">
      <h2 class="head" style="font-size:13px">Trusted, Personalized<br>&amp; Affordable Dental Care<br>for Your Whole Family</h2>
      <p class="sub" style="margin-top:12px">Cleanings Help Protect You &amp;<br>Your Family From:</p>
      <p class="body" style="text-align:left;margin:10px 0 0 10px;line-height:1.7">• Low-Cost Dental Coverage for Uninsured Patients<br>• Convenient Hours ~ Never Miss Work or School!<br>• 0% Financing Available</p>
      <div style="margin-top:24px"><span class="brand" style="font-size:12px"><span class="brand-dot"></span>Maple Ridge Family Dental</span></div>
      <h3 class="head" style="margin-top:22px;font-size:13px">Walk In! You're<br>Always Welcome!</h3>
      <p class="sub" style="margin-top:18px;font-size:6.5px">212 Linden Street, Suite 4 • Brookfield</p>
      <p class="body" style="margin-top:4px">We are located on Linden Street &amp; Pine Road, just off of<br>Route 12, on the 2nd floor of the Holloway &amp; Brandt building.</p>
      <p style="font-family:var(--serif);font-weight:700;font-size:17px;margin-top:22px">555-214-3860</p>
      <p style="font-family:var(--serif);font-weight:700;font-size:7px;margin-top:4px">www.MapleRidgeFamilyDental.com</p>
    </div>
  </div>

  <div class="panel panel--services">
    <div style="padding:18px 0 0">
      <h2 class="head" style="font-size:18px">One Office for All<br>Your Dental Needs</h2>
      <p class="body" style="text-align:left;padding:0 16px;margin-top:8px">The Latest Procedures, Instruments &amp;<br>Techniques Gentle Private-Practice Dentists</p>
      <ul class="list" style="margin-top:8px">
        <li>Sealants &amp; Fluoride Treatments<br>Low-Radiation Digital X-Rays</li>
        <li>Laser-Assisted Dental Treatment Infrared<br>Cavity Diagnosis</li>
        <li>Root Canal Treatments Bridges &amp; Implants</li>
        <li>Dentures</li>
        <li>FILLARA™</li>
        <li>CONTOURIN™ We Offer Nitrous Oxide &amp; Free<br>Whitening For Life!</li>
      </ul>
      <h3 class="head" style="margin-top:10px;font-size:13px">Cosmetic Dentistry Can<br>Change Your Life!</h3>
      <p class="body" style="margin-top:5px">Mercury-Free Dentistry • GlowBright Teeth<br>Whitening Crowns • Veneers</p>
      <div style="margin-top:8px"><span class="cta">Call us today for more details.</span></div>
      <h3 class="head" style="margin-top:10px;font-size:11.5px">Reduce Wrinkles With<br>SMOOTHA® &amp; DERMAVEL®!</h3>
      <p class="body" style="margin-top:5px">Look Younger • Takes Only 10 Minutes<br>No Recovery Time</p>
      <p class="body" style="margin-top:9px">Restore youthful contours to the skin &amp; smooth<br>away moderate to severe wrinkles &amp; folds.<br>Call today for your appointment.</p>
    </div>
  </div>
</section>

</body>
</html>
```